Grand Opening / Live Music Event

My band is playing a Grand Opening event on Saturday April 5th. I need a flyer utilizing the attached image of our bass player and incorporating our band logo. This picture makes me laugh and gives the impression he is angry - like saying "it's going to be a celebration fool!" or something along those lines. I need to the flyer to pop and present an image that it will be an excellent party. Feel free to incorporate any background or theme style. You can find other images of my band in the event they are needed at: https://www.velorumhub.example/Corkvalleyband

Some details:

The event will be at Quimby's Hall. 8241 Larkspur Ave. #204, Frisco, Texas. (214) 705-9183 for table reservations.

Saturday April 5th. Party starts at 7:00 PM with an acoustic set by the Velvet Otters and Cork Valley taking the stage at 10:00 PM.

Hottest new bar in Frisco! Drink specials all night with the Zephyr Pale girls, and great live music to celebrate this grand opening.

I will use this for FB and other online marketing, as well as some print.

```html
<!DOCTYPE html>
<html lang="en">
<head>
<meta charset="utf-8">
<title>Grand Opening – Quimby's Hall</title>
<link rel="stylesheet" href="https://fonts.googleapis.com/css2?family=Bungee+Inline&family=Ultra&family=Alfa+Slab+One&family=Varela+Round&family=Questrial&display=block">
<style>
  :root {
    --paper: #ffffff;
    --shadow-grey: #c9c9c9;
    --ink: #1d1d1d;
    --cream: #f6efe0;
    --venue-red: #8a2f3f;
    --ready-green: #3fae55;
    --date-green: rgba(62, 170, 110, 0.85);
    --act-magenta: rgba(150, 40, 120, 0.9);
    --time-yellow: #f4d323;
    --cassette-teal: #9ad9d8;
    --cassette-body: #2b2b2b;
    --frame-line: rgba(255, 255, 255, 0.8);
    --slab: "Ultra", "Alfa Slab One", "Rockwell Extra Bold", "Rockwell", Georgia, serif;
  }
  * { margin: 0; padding: 0; box-sizing: border-box; }
  html, body { width: 898px; height: 1200px; overflow: hidden; background: var(--paper); }
  .canvas { position: relative; width: 898px; height: 1200px; background: var(--paper); }
  .backing { position: absolute; left: 0; top: 0; width: 829px; height: 1200px; background: var(--shadow-grey); }
  .flyer { position: absolute; left: 26px; top: 0; width: 795px; height: 1142px; overflow: hidden; background: #5d4a8c; }
  .block { position: absolute; }

  .pattern-top { left: 0; top: 0; width: 795px; height: 185px;
    background: linear-gradient(90deg, #e23d9a 0%, #b9b3c0 25%, #e75a9c 45%, #a8a0b4 62%, #48b85a 82%, #d74fa0 100%); }
  .title-band { left: 0; top: 44px; width: 795px; height: 102px; background: rgba(215, 215, 220, 0.72); }
  .pattern-left { left: 0; top: 185px; width: 148px; height: 842px;
    background: linear-gradient(180deg, #e2a158 0%, #9b7a4a 18%, #e59653 36%, #c44a62 58%, #ea6f7b 78%, #d9785e 100%); }
  .pattern-right { left: 660px; top: 185px; width: 135px; height: 842px;
    background: linear-gradient(180deg, #9a6cd3 0%, #7b5bc4 30%, #9365c7 55%, #6f4ea9 100%); }
  .pattern-bottom { left: 0; top: 1023px; width: 795px; height: 119px;
    background: linear-gradient(90deg, #7f8fd6 0%, #6a74c8 35%, #8b7cd0 65%, #6b6fc6 100%); }

  .title { position: absolute; left: 0; top: 46px; width: 795px; text-align: center;
    font-family: "Bungee Inline", "Alfa Slab One", sans-serif; font-size: 78px; line-height: 96px;
    letter-spacing: 3px; color: var(--ink); font-weight: 400; }

  .venue-box { left: 120px; top: 186px; width: 512px; height: 98px; background: var(--venue-red);
    border: 2px solid var(--frame-line); display: flex; align-items: center; justify-content: center; }
  .venue-name { font-family: var(--slab); font-size: 48px; font-weight: 900; color: var(--cream); white-space: nowrap; }
  .ready-box { left: 632px; top: 186px; width: 186px; height: 98px; background: var(--ready-green);
    border: 2px solid var(--frame-line); display: flex; align-items: center; justify-content: center; text-align: center; }
  .ready-text { font-family: "Varela Round", sans-serif; font-size: 29px; line-height: 1.15; color: var(--cream); }

  .band-photo { left: 120px; top: 288px; width: 566px; height: 735px;
    background:
      radial-gradient(ellipse 40% 30% at 48% 38%, rgba(196, 56, 94, 0.85) 0%, rgba(196, 56, 94, 0) 100%),
      radial-gradient(ellipse 45% 30% at 40% 88%, rgba(205, 180, 230, 0.7) 0%, rgba(205, 180, 230, 0) 100%),
      linear-gradient(180deg, #20295e 0%, #2b2f6b 50%, #3a2d72 100%);
    border: 2px solid var(--frame-line); }

  .date-box { left: 0; top: 601px; width: 423px; height: 112px; background: var(--date-green);
    border: 2px solid var(--frame-line); display: flex; align-items: center; justify-content: center; }
  .date-text { font-family: var(--slab); font-weight: 900; font-size: 58px; color: var(--cream); white-space: nowrap; }
  .opener-box { left: 423px; top: 607px; width: 372px; height: 99px; background: var(--act-magenta);
    border: 2px solid var(--frame-line); display: flex; align-items: center; justify-content: center; text-align: center; }
  .opener-text { font-family: var(--slab); font-weight: 900; font-size: 30px; line-height: 1.05; color: var(--cream); }

  .cassette-art { left: 430px; top: 716px; width: 360px; height: 224px; border-radius: 14px;
    background: var(--cassette-teal); border: 8px solid var(--cassette-body); }
  .headliner { position: absolute; left: 423px; top: 882px; width: 372px; text-align: center;
    font-family: var(--slab); font-weight: 900; font-size: 42px; line-height: 56px; color: var(--cream);
    white-space: nowrap; }
  .time-box { left: 423px; top: 944px; width: 372px; height: 79px; background: var(--time-yellow);
    border: 2px solid var(--frame-line); display: flex; align-items: center; justify-content: center; }
  .time-text { font-family: var(--slab); font-weight: 900; font-size: 52px; color: var(--ink); }

  .details { position: absolute; left: 178px; top: 1046px; font-family: "Questrial", sans-serif;
    font-size: 26px; line-height: 38px; color: var(--ink); }
</style>
</head>
<body>
<div class="canvas">
  <div class="backing"></div>
  <div class="flyer">
    <div class="block pattern-top" role="img" aria-label="Colourful dotted pattern band"></div>
    <div class="block title-band"></div>
    <div class="block pattern-left" role="img" aria-label="Warm dotted pattern strip"></div>
    <div class="block pattern-right" role="img" aria-label="Purple dotted pattern strip"></div>
    <div class="block pattern-bottom" role="img" aria-label="Blue dotted pattern band"></div>

    <h1 class="title">GRAND OPENING</h1>

    <div class="block band-photo" role="img" aria-label="Photo of the bass player performing on stage"></div>

    <div class="block venue-box"><span class="venue-name">QUIMBY'S HALL</span></div>
    <div class="block ready-box"><span class="ready-text">are you<br>ready?</span></div>

    <div class="block date-box"><span class="date-text">APRIL 5TH</span></div>
    <div class="block opener-box"><span class="opener-text">VELVET OTTERS<br>AT 7:00PM</span></div>

    <div class="block cassette-art" role="img" aria-label="Illustration of a mix tape cassette"></div>
    <div class="headliner">CORK VALLEY</div>
    <div class="block time-box"><span class="time-text">10:00PM!</span></div>

    <p class="details">8241 Larkspur Ave. #204, Frisco, Texas<br>(214) 705-9183 for table reservations</p>
  </div>
</div>
</body>
</html>
```